Verpackungsdesign für Pasta aus Buchweizen
Zielgruppe
Unser Unternehmen KORNIVA sucht ein sehr modernes Verpackungsdesign für Pasta aus Buchweizen.
Unsere Produkte sind in unserem Online Shop und unterscheiden sich durch die herkömmliche Pasta, da wir Buchweizen in die Verarbeitung mit aufnehmen und somit die gesundheitsfördernde Eigenschaft des Buchweizens im Vordergrund steht. Unsere Pasta aus Buchweizenmehl mit klassischem Hartweizengrieß ist in dieser Form noch nicht im stationären Handel erhältlich, deshalb wünschen wir uns ein neues, ansprechendes Verpackungsdesign welches von den Massenprodukten aus den Regalen im Handel heraussticht. Das Design sollte also minimalistisch und sehr modern wirken, und sich deutlich von der Konkurrenz abheben.
Die Zielgruppe richtet sich sowohl an Massen die Pasta in allen Variationen lieben, als auch an ernährungsbewusste Veganer/Vegetarier die Alternativen im Bereich der herkömmlichen Pasta Kochkultur suchen.
PS: Mit dem Verkauf unserer Pasta investieren wir außerdem in den Aufbau und der Infrastruktur des Erzeugerlandes. Durch unser Prinzip „Teilen & Wachsen“ fördern wir mit unseren Gewinnen nachhaltige Projekte in den Erzeugerländern und helfen somit wirtschaftlich benachteiligten Regionen auf der Welt. (Fair Trade)
Aufgabenstellung
Wir besitzen bereits ein Logo und Verpackungen für unsere Pasta Sorten. Das Logo und das Grundgerüst der Stanzform / Verpackungsmaße (inkl. Sichtfenster) soll beibehalten werden (Siehe Anhang). Als Pasta Verpackungen benutzen wir Faltschachteln und Banderolen.
Verpackungsmaße:
- Faltschachtel (90 x 40 x 165 mm)
- Banderole (560 x 70mm)
Der Produktname ist je nach Sorte zu präzisieren:
- Fusilli
- Makkaroni
- Bandnudeln
- Tarhana
Produktgewicht:
- 250g
Eigenschaften:
- Buchweizenmehl
- 100% Vegan
- Kochzeit 3 Minuten
- Liebevolle Handarbeit
WICHTIG:
1) Bitte benutzt die hochgeladene, leere Stanzform für Artwork.
2) Die Designfarbe kann anhand des Aufstellers ausgerichtet werden (CMYK: 0, 20, 32, 0 und 60, 57, 56, 62) es ist aber kein muss und ihr seit frei in der Kreativität.
3) Bitte das Sichtfenster mit Rand wie aktuell auf den Produkten übernehmen (siehe www.korniva.de/shop)
Nach dem Wettbewerb planen wir zusätzlich ein 1zu1 Projekt und würden uns freuen einen Gewinner auszuwählen - Wir freuen uns auf eure Ideen :)

```html
<!DOCTYPE html>
<html lang="de">
<head>
<meta charset="utf-8">
<title>KORNIVA Buchweizen Pasta – Faltschachteln</title>
<link rel="stylesheet" href="https://fonts.googleapis.com/css2?family=Antonio:wght@200;700&family=Montserrat:wght@200;300;400;500&family=Dancing+Script:wght@500&display=swap">
<style>
  :root {
    --page: #ffffff;
    --stage: #dedede;
    --stage-label: #f7f7f7;
    --carton-white: #ffffff;
    --side-white: #f1f1f1;
    --blush: #ecd4c7;
    --blush-side: #e6cbbd;
    --ink: #3d3636;
    --ink-soft: #6e6464;
    --vegan-green: #3f9a4a;
  }
  * { box-sizing: border-box; margin: 0; padding: 0; }
  html, body { width: 1200px; height: 3250px; overflow: hidden; background: var(--page); }
  body { position: relative; font-family: "Montserrat", sans-serif; color: var(--ink); }

  .variant {
    position: absolute; left: 82px; width: 1034px; height: 997px;
    background: var(--stage);
  }
  .variant--tarhana { top: 66px; }
  .variant--makkaroni { top: 1129px; }
  .variant--fusilli { top: 2193px; }

  .range-title {
    position: absolute; left: 600px; top: 340px;
    font-family: "Montserrat", sans-serif; font-weight: 200;
    font-size: 36px; line-height: 44px; letter-spacing: 15px;
    color: var(--stage-label);
  }

  .carton { position: absolute; left: 120px; top: 185px; height: 620px; display: flex; }

  /* side panel */
  .carton-side { width: 150px; height: 100%; display: flex; flex-direction: column; }
  .carton-side__top {
    height: 210px; background: var(--side-white);
    display: flex; flex-direction: column; align-items: center; padding-top: 110px;
  }
  .cook-time {
    font-family: "Montserrat", sans-serif; font-weight: 300; font-size: 14px;
    line-height: 17px; text-align: center; color: var(--ink); text-transform: uppercase;
  }
  .pot-icon { width: 58px; height: 58px; margin-top: 10px; }
  .carton-side__bottom {
    flex: 1; background: var(--blush-side); padding: 26px 16px 20px;
    display: flex; flex-direction: column; position: relative;
  }
  .side-copy {
    font-family: "Montserrat", sans-serif; font-size: 7.5px; line-height: 10px;
    color: var(--ink-soft); text-align: justify; margin-bottom: 12px;
  }
  .vegan-badge {
    width: 36px; height: 36px; border-radius: 50%;
    border: 3px solid var(--vegan-green); background: #ffffff;
    margin-top: auto; margin-left: 30px;
  }
  .net-weight {
    font-family: "Montserrat", sans-serif; font-weight: 300; color: var(--ink);
  }
  .carton-side .net-weight { font-size: 13px; margin-top: 26px; margin-left: 30px; }

  /* front panel */
  .carton-front { width: 340px; height: 100%; display: flex; flex-direction: column; }
  .carton-front__top {
    height: 210px; background: var(--carton-white); position: relative;
  }
  .brand {
    position: absolute; left: 0; right: 0; top: 40px;
    display: flex; align-items: center; justify-content: center; gap: 8px;
  }
  .brand__dot { width: 12px; height: 12px; border-radius: 50%; background: #d89a72; }
  .brand__name {
    font-family: "Antonio", sans-serif; font-weight: 700; font-size: 20px;
    letter-spacing: 1px; color: var(--ink);
  }
  .product-name { position: absolute; left: 30px; top: 92px; width: 290px; }
  .product-name__main {
    display: block; font-family: "Antonio", sans-serif; font-weight: 200;
    font-size: 66px; line-height: 62px; letter-spacing: 0; color: var(--ink);
  }
  .product-name__sub {
    display: flex; align-items: flex-start; gap: 6px;
  }
  .product-name__pasta {
    font-family: "Antonio", sans-serif; font-weight: 700; font-size: 54px;
    line-height: 54px; color: var(--ink);
  }
  .product-name__en {
    font-family: "Montserrat", sans-serif; font-weight: 300; font-size: 8.5px;
    letter-spacing: 6px; color: var(--ink-soft); margin-top: 2px;
  }
  .carton-front__bottom {
    flex: 1; background: var(--blush); position: relative; padding: 42px 30px 0;
  }
  .variety {
    font-family: "Montserrat", sans-serif; font-weight: 300; font-size: 30px;
    line-height: 34px; color: #ffffff;
  }
  .variety-note {
    font-family: "Dancing Script", cursive; font-size: 18px; color: var(--ink); margin-top: 2px;
  }
  .window {
    position: absolute; left: 40px; top: 110px; width: 200px; height: 250px;
    border-radius: 120px 8px 120px 8px;
  }
  .window--tarhana { background: linear-gradient(150deg, #c88a5d, #9e5e37); }
  .window--makkaroni { background: linear-gradient(150deg, #d8b08c, #a97c58); }
  .window--fusilli { background: linear-gradient(150deg, #a0785a, #6b4a33); }
  .carton-front .net-weight { position: absolute; right: 20px; bottom: 84px; font-size: 19px; }
</style>
</head>
<body>

<section class="variant variant--tarhana">
  <div class="carton">
    <div class="carton-side">
      <div class="carton-side__top">
        <p class="cook-time">Kochzeit<br>3 Minuten</p>
        <svg class="pot-icon" viewBox="0 0 60 60" fill="none" stroke="#3d3636" stroke-width="2.2" stroke-linecap="round">
          <path d="M14 24h32v16a6 6 0 0 1-6 6H20a6 6 0 0 1-6-6z"/>
          <path d="M10 26h4M46 26h4M22 20h16M30 16v4"/>
          <path d="M44 14c2-2 0-4 2-6M50 16c2-2 0-4 2-6"/>
          <path d="M22 52v3M30 52v3M38 52v3"/>
        </svg>
      </div>
      <div class="carton-side__bottom">
        <p class="side-copy">Buchweizenmehl und Hartweizengrieß, in Handarbeit zu feiner Pasta verarbeitet.</p>
        <p class="side-copy">Wasser aufkochen, salzen, Pasta einlegen und drei Minuten garen. Abgießen und servieren.</p>
        <p class="side-copy">Trocken und kühl lagern. Nach dem Öffnen gut verschließen. Mit jedem Kauf fördern wir nachhaltige Projekte in den Erzeugerländern.</p>
        <span class="vegan-badge" role="img" aria-label="Vegan-Siegel"></span>
        <p class="net-weight">250g ℮</p>
      </div>
    </div>
    <div class="carton-front">
      <div class="carton-front__top">
        <div class="brand"><span class="brand__dot"></span><span class="brand__name">KORNIVA</span></div>
        <h2 class="product-name">
          <span class="product-name__main">BUCHWEIZEN</span>
          <span class="product-name__sub"><span class="product-name__pasta">PASTA</span><span class="product-name__en">BUCKWHEAT</span></span>
        </h2>
      </div>
      <div class="carton-front__bottom">
        <p class="variety">tarhana</p>
        <p class="variety-note">für Suppen</p>
        <div class="window window--tarhana" role="img" aria-label="Sichtfenster in Blattform mit Blick auf Tarhana aus Buchweizen"></div>
        <p class="net-weight">250g ℮</p>
      </div>
    </div>
  </div>
  <p class="range-title">BUCHWEIZEN<br>PASTA</p>
</section>

<section class="variant variant--makkaroni">
  <div class="carton">
    <div class="carton-side">
      <div class="carton-side__top">
        <p class="cook-time">Kochzeit<br>3 Minuten</p>
        <svg class="pot-icon" viewBox="0 0 60 60" fill="none" stroke="#3d3636" stroke-width="2.2" stroke-linecap="round">
          <path d="M14 24h32v16a6 6 0 0 1-6 6H20a6 6 0 0 1-6-6z"/>
          <path d="M10 26h4M46 26h4M22 20h16M30 16v4"/>
          <path d="M44 14c2-2 0-4 2-6M50 16c2-2 0-4 2-6"/>
          <path d="M22 52v3M30 52v3M38 52v3"/>
        </svg>
      </div>
      <div class="carton-side__bottom">
        <p class="side-copy">Buchweizenmehl und Hartweizengrieß, in Handarbeit zu feiner Pasta verarbeitet.</p>
        <p class="side-copy">Wasser aufkochen, salzen, Pasta einlegen und drei Minuten garen. Abgießen und servieren.</p>
        <p class="side-copy">Trocken und kühl lagern. Nach dem Öffnen gut verschließen. Mit jedem Kauf fördern wir nachhaltige Projekte in den Erzeugerländern.</p>
        <span class="vegan-badge" role="img" aria-label="Vegan-Siegel"></span>
        <p class="net-weight">250g ℮</p>
      </div>
    </div>
    <div class="carton-front">
      <div class="carton-front__top">
        <div class="brand"><span class="brand__dot"></span><span class="brand__name">KORNIVA</span></div>
        <h2 class="product-name">
          <span class="product-name__main">BUCHWEIZEN</span>
          <span class="product-name__sub"><span class="product-name__pasta">PASTA</span><span class="product-name__en">BUCKWHEAT</span></span>
        </h2>
      </div>
      <div class="carton-front__bottom">
        <p class="variety">makkaroni</p>
        <div class="window window--makkaroni" role="img" aria-label="Sichtfenster in Blattform mit Blick auf Makkaroni aus Buchweizen"></div>
        <p class="net-weight">250g ℮</p>
      </div>
    </div>
  </div>
  <p class="range-title">BUCHWEIZEN<br>PASTA</p>
</section>

<section class="variant variant--fusilli">
  <div class="carton">
    <div class="carton-side">
      <div class="carton-side__top">
        <p class="cook-time">Kochzeit<br>3 Minuten</p>
        <svg class="pot-icon" viewBox="0 0 60 60" fill="none" stroke="#3d3636" stroke-width="2.2" stroke-linecap="round">
          <path d="M14 24h32v16a6 6 0 0 1-6 6H20a6 6 0 0 1-6-6z"/>
          <path d="M10 26h4M46 26h4M22 20h16M30 16v4"/>
          <path d="M44 14c2-2 0-4 2-6M50 16c2-2 0-4 2-6"/>
          <path d="M22 52v3M30 52v3M38 52v3"/>
        </svg>
      </div>
      <div class="carton-side__bottom">
        <p class="side-copy">Buchweizenmehl und Hartweizengrieß, in Handarbeit zu feiner Pasta verarbeitet.</p>
        <p class="side-copy">Wasser aufkochen, salzen, Pasta einlegen und drei Minuten garen. Abgießen und servieren.</p>
        <p class="side-copy">Trocken und kühl lagern. Nach dem Öffnen gut verschließen. Mit jedem Kauf fördern wir nachhaltige Projekte in den Erzeugerländern.</p>
        <span class="vegan-badge" role="img" aria-label="Vegan-Siegel"></span>
        <p class="net-weight">250g ℮</p>
      </div>
    </div>
    <div class="carton-front">
      <div class="carton-front__top">
        <div class="brand"><span class="brand__dot"></span><span class="brand__name">KORNIVA</span></div>
        <h2 class="product-name">
          <span class="product-name__main">BUCHWEIZEN</span>
          <span class="product-name__sub"><span class="product-name__pasta">PASTA</span><span class="product-name__en">BUCKWHEAT</span></span>
        </h2>
      </div>
      <div class="carton-front__bottom">
        <p class="variety">fusilli</p>
        <div class="window window--fusilli" role="img" aria-label="Sichtfenster in Blattform mit Blick auf Fusilli aus Buchweizen"></div>
        <p class="net-weight">250g ℮</p>
      </div>
    </div>
  </div>
  <p class="range-title">BUCHWEIZEN<br>PASTA</p>
</section>

</body>
</html>
```